Stylish new business card needed!

Hello everyone! I am in need of a new business card design for an alarm company here in Hurricane WV. I have all fonts, color codes and logos provided for you use! We are a young company and like the style of a clean sleek looking business card. Would like it double sided, one side holding the logo and the other with your design!
Target Market(s)
The people that are looking for the newest tech for home automation and security
Industry/Entity Type
Alarm services; Home automation
Contact Information for Business Card
Name of person; position (Sales; Installer); Phone Number (555.418.7290); Employee cell Number; Website (www.GuardedByVemlo.example); Employee Email; Double sided
Look and feel
Each slider illustrates characteristics of the customer's brand and the style your logo design should communicate.

```html
<!DOCTYPE html>
<html lang="en">
<head>
<meta charset="utf-8">
<title>Guarded by Vemlo – Business Card</title>
<link href="https://fonts.googleapis.com/css2?family=Lato:wght@400;700;900&display=swap" rel="stylesheet">
<style>
  :root {
    --bg: #e9e6e2;
    --card: #1d1d1d;
    --card-shadow: rgba(0,0,0,0.25);
    --orange: #f58a3c;
    --grey-text: #c9c9c9;
    --deco: #2a2a2a;
  }
  * { margin: 0; padding: 0; box-sizing: border-box; }
  html, body {
    width: 1200px; height: 977px; overflow: hidden;
    background: var(--bg);
    font-family: "Lato", Arial, sans-serif;
  }
  .canvas {
    position: relative; width: 1200px; height: 977px;
  }
  .card {
    position: absolute; left: 250px;
    width: 700px; height: 400px;
    background: var(--card);
    border-radius: 22px;
    box-shadow: 0 10px 30px var(--card-shadow);
    overflow: hidden;
  }
  .card--front { top: 70px; }
  .card--back { top: 507px; }

  /* front */
  .brand {
    position: absolute; left: 0; right: 0; top: 110px;
    text-align: center; color: var(--orange); font-weight: 900;
  }
  .brand__lead { font-size: 34px; letter-spacing: 2px; }
  .brand__name { font-size: 96px; line-height: 1; letter-spacing: 6px; margin-top: 4px; }
  .brand__tagline {
    font-size: 15px; letter-spacing: 1.5px; margin-top: 18px;
  }

  /* back */
  .back__wordmark {
    position: absolute; right: 24px; top: -20px;
    font-size: 170px; font-weight: 900; letter-spacing: 8px;
    color: var(--deco); line-height: 1;
  }
  .person { position: absolute; left: 70px; bottom: 70px; }
  .person__name {
    color: var(--orange); font-weight: 900; font-size: 34px; letter-spacing: 0.5px;
  }
  .person__role { color: var(--grey-text); font-size: 22px; margin-top: 2px; }
  .person__rule {
    width: 30px; height: 4px; background: var(--orange); margin-top: 14px;
  }
  .contact {
    position: absolute; right: 40px; bottom: 90px;
    list-style: none; color: var(--grey-text); font-size: 17px;
  }
  .contact li { display: flex; align-items: center; gap: 12px; margin-top: 8px; }
  .contact svg { width: 15px; height: 15px; fill: var(--orange); flex: none; }
</style>
</head>
<body>
<main class="canvas">

  <section class="card card--front" aria-label="Card front">
    <div class="brand">
      <div class="brand__lead">GUARDED BY</div>
      <div class="brand__name">VEMLO</div>
      <div class="brand__tagline">AUTOMATION AND SECURITY SERVICES</div>
    </div>
  </section>

  <section class="card card--back" aria-label="Card back">
    <div class="back__wordmark" aria-hidden="true">VEMLO</div>

    <div class="person">
      <div class="person__name">DANIEL HARPER</div>
      <div class="person__role">Sales &amp; Installer</div>
      <div class="person__rule"></div>
    </div>

    <ul class="contact">
      <li>
        <svg viewBox="0 0 16 16" aria-hidden="true"><path d="M3 1l3 3-2 2c1 2 3 4 5 5l2-2 3 3-2 3C7 15 1 9 1 3z"/></svg>
        555.418.7290
      </li>
      <li>
        <svg viewBox="0 0 16 16" aria-hidden="true"><path d="M4 0h8v16H4zM5.5 2v10h5V2zM7 13h2v1.5H7z" fill-rule="evenodd"/></svg>
        555.418.7291
      </li>
      <li>
        <svg viewBox="0 0 16 16" aria-hidden="true"><path d="M1 3h14v10H1zM1 3l7 6 7-6"/></svg>
        daniel@guardedbyvemlo.example
      </li>
      <li>
        <svg viewBox="0 0 16 16" aria-hidden="true"><circle cx="8" cy="8" r="7"/></svg>
        www.GuardedByVemlo.example
      </li>
    </ul>
  </section>

</main>
</body>
</html>
```